Marrowgate Auctions Business Cards Design Needed

I need a business card design that is modern looking - double sided (maybe just my logo on the back, but open to suggestions) - the overall design is up to you. I want it to be easy to read - not over the top flashy. I already have a company logo which I uploaded so that needs to be used. The colors of my logo are the colors I want on the card... so blue and gray (do need to match the logo colors).

Requirements
Must have
• Would like the card to be sleek, modern and easy to ready

```html
<!DOCTYPE html>
<html lang="en">
<head>
<meta charset="utf-8">
<title>Marrowgate Auctions Business Cards</title>
<link rel="stylesheet" href="https://fonts.googleapis.com/css2?family=Montserrat:wght@400;500;700&display=swap">
<style>
  :root {
    --stage: #2a2c30;
    --card-dark: #0b0b0c;
    --card-light: #ffffff;
    --brand-blue: #1a7fc8;
    --brand-gray: #5f6064;
    --band-gray: #46474b;
    --text-gray: #4a4b4f;
  }
  * { margin: 0; padding: 0; box-sizing: border-box; }
  html, body {
    width: 1200px; height: 900px; overflow: hidden;
    background: var(--stage);
    font-family: "Montserrat", Arial, sans-serif;
  }
  .stage {
    position: relative; width: 1200px; height: 900px;
    display: flex; align-items: center; justify-content: center; gap: 50px;
  }
  .card {
    position: relative; width: 525px; height: 300px;
    border-radius: 4px; overflow: hidden;
    box-shadow: 0 12px 30px rgba(0,0,0,.35);
  }
  /* Back side */
  .card--back {
    background: var(--card-dark);
    display: flex; flex-direction: column; align-items: center; justify-content: center;
  }
  .brand-lockup { display: flex; align-items: center; gap: 14px; }
  .brand-lockup__dot {
    width: 26px; height: 26px; border-radius: 50%; background: var(--brand-blue);
  }
  .brand-lockup__name {
    font-weight: 700; font-size: 30px; letter-spacing: .5px;
    color: var(--brand-gray); text-transform: uppercase;
  }
  .tagline {
    margin-top: 18px; font-size: 14px; font-weight: 400;
    color: var(--brand-blue); letter-spacing: .3px;
  }
  /* Front side */
  .card--front { background: var(--card-light); }
  .edge-band {
    position: absolute; right: 0; top: 0; width: 22px; height: 100%;
    background: linear-gradient(to bottom, var(--band-gray) 0 48%, var(--brand-blue) 48% 100%);
  }
  .contact-block { position: absolute; left: 34px; top: 32px; }
  .person-name {
    font-weight: 700; font-size: 18px; color: var(--brand-blue); letter-spacing: .3px;
  }
  .person-title { font-size: 12.5px; color: var(--text-gray); margin-top: 2px; }
  .company-name {
    font-weight: 700; font-size: 14px; color: var(--brand-blue); margin-top: 22px;
  }
  .contact-list { list-style: none; margin-top: 8px; }
  .contact-list li {
    display: flex; align-items: center; gap: 10px;
    font-size: 13px; color: var(--text-gray); line-height: 24px;
  }
  .contact-list svg { width: 13px; height: 13px; fill: var(--brand-blue); flex: none; }
  .front-mark {
    position: absolute; right: 48px; bottom: 34px;
    display: flex; align-items: center; gap: 8px;
  }
  .front-mark__square { width: 14px; height: 14px; background: var(--brand-blue); }
  .front-mark__name { font-weight: 700; font-size: 15px; color: var(--brand-blue); }
</style>
</head>
<body>
<main class="stage">
  <section class="card card--back" aria-label="Card back">
    <div class="brand-lockup">
      <span class="brand-lockup__dot"></span>
      <span class="brand-lockup__name">Marrowgate Auctions</span>
    </div>
    <p class="tagline">Improving Charity Auctions Nationwide</p>
  </section>

  <section class="card card--front" aria-label="Card front">
    <div class="contact-block">
      <h1 class="person-name">OWEN HARTLEY</h1>
      <p class="person-title">Owner/President - Auctioneer</p>
      <h2 class="company-name">Marrowgate Auctions, Inc.</h2>
      <ul class="contact-list">
        <li>
          <svg viewBox="0 0 24 24" aria-hidden="true"><path d="M6.6 10.8a15.1 15.1 0 0 0 6.6 6.6l2.2-2.2a1 1 0 0 1 1-.25 11.4 11.4 0 0 0 3.6.57 1 1 0 0 1 1 1V20a1 1 0 0 1-1 1A17 17 0 0 1 3 4a1 1 0 0 1 1-1h3.5a1 1 0 0 1 1 1c0 1.25.2 2.45.57 3.6a1 1 0 0 1-.25 1z"/></svg>
          702-555-0148
        </li>
        <li>
          <svg viewBox="0 0 24 24" aria-hidden="true"><path d="M2 5h20v14H2z" fill="none"/><path d="M2 5h20v2l-10 6L2 7zM2 9l10 6 10-6v10H2z"/></svg>
          hello@marrowgateauctions.com
        </li>
        <li>
          <svg viewBox="0 0 24 24" aria-hidden="true"><path d="M12 2a10 10 0 1 0 0 20 10 10 0 0 0 0-20zm6.9 6h-3a15.6 15.6 0 0 0-1.4-3.6A8 8 0 0 1 18.9 8zM12 4c.8 1.2 1.5 2.5 1.9 4h-3.8c.4-1.5 1.1-2.8 1.9-4zM4.3 14a8.2 8.2 0 0 1 0-4h3.4a16.5 16.5 0 0 0 0 4zm.8 2h3a15.6 15.6 0 0 0 1.4 3.6A8 8 0 0 1 5.1 16zm3-8h-3a8 8 0 0 1 4.4-3.6A15.6 15.6 0 0 0 8.1 8zM12 20c-.8-1.2-1.5-2.5-1.9-4h3.8c-.4 1.5-1.1 2.8-1.9 4zm2.3-6H9.7a14.7 14.7 0 0 1 0-4h4.6a14.7 14.7 0 0 1 0 4zm.2 5.6c.6-1.1 1.1-2.3 1.4-3.6h3a8 8 0 0 1-4.4 3.6zm1.8-5.6a16.5 16.5 0 0 0 0-4h3.4a8.2 8.2 0 0 1 0 4z"/></svg>
          www.gavelrevival.com
        </li>
      </ul>
    </div>
    <div class="front-mark">
      <span class="front-mark__square"></span>
      <span class="front-mark__name">Marrowgate Auctions</span>
    </div>
    <div class="edge-band"></div>
  </section>
</main>
</body>
</html>
```